Letter Head Design

I need a letter head design based on my company logo that I attached.
Include phone number: (403)582-4316
Address: 347 14th Avenue NE, Calgary, Alberta, Canada, T3K 4R8

Industry/Entity Type

It Company

```html
<!DOCTYPE html>
<html lang="en">
<head>
<meta charset="utf-8">
<title>Brightroom Interiors Corp. – Letterhead</title>
<link rel="stylesheet" href="https://fonts.googleapis.com/css2?family=Open+Sans:wght@400;600&display=swap">
<style>
  :root {
    --paper: #ffffff;
    --ink: #1a1a1a;
    --brand-blue: #2a6fd6;
    --brand-green: #7ed321;
    --rule-blue: #3c7fe0;
    --divider: #c9d6ea;
  }
  html, body {
    margin: 0;
    padding: 0;
    width: 956px;
    height: 1200px;
    overflow: hidden;
    background: var(--paper);
  }
  .letterhead {
    position: relative;
    width: 956px;
    height: 1200px;
    background: var(--paper);
    font-family: "Open Sans", Arial, sans-serif;
    color: var(--ink);
  }
  .brand {
    position: absolute;
    top: 88px;
    left: 0;
    width: 100%;
    display: flex;
    justify-content: center;
    align-items: center;
    gap: 12px;
  }
  .brand-square {
    width: 30px;
    height: 30px;
    background: var(--brand-green);
  }
  .brand-name {
    font-size: 26px;
    font-weight: 600;
    color: var(--brand-blue);
    letter-spacing: -0.3px;
  }
  .footer-rule {
    position: absolute;
    top: 1124px;
    left: 313px;
    width: 328px;
    height: 3px;
  }
  .contact-line {
    position: absolute;
    top: 1144px;
    left: 0;
    width: 100%;
    display: flex;
    justify-content: center;
    align-items: center;
    gap: 20px;
    font-size: 16px;
    font-weight: 400;
    white-space: nowrap;
  }
  .contact-divider {
    width: 1px;
    height: 16px;
    background: var(--divider);
  }
</style>
</head>
<body>
  <div class="letterhead">
    <header class="brand">
      <span class="brand-square"></span>
      <span class="brand-name">Brightroom Interiors Corp.</span>
    </header>

    <svg class="footer-rule" viewBox="0 0 328 3" preserveAspectRatio="none" aria-hidden="true">
      <defs>
        <linearGradient id="ruleFade" x1="0" x2="1" y1="0" y2="0">
          <stop offset="0" stop-color="#3c7fe0" stop-opacity="0.1"/>
          <stop offset="0.5" stop-color="#3c7fe0" stop-opacity="1"/>
          <stop offset="1" stop-color="#3c7fe0" stop-opacity="0.1"/>
        </linearGradient>
      </defs>
      <rect x="0" y="0" width="328" height="2" fill="url(#ruleFade)"/>
    </svg>

    <footer class="contact-line">
      <span class="contact-phone">P: 403-582-4316</span>
      <span class="contact-divider"></span>
      <span class="contact-address">A: 347 14th Avenue NE, Calgary, Alberta, Canada, T3K 4R8</span>
    </footer>
  </div>
</body>
</html>
```